Home Health Care Agency Needs a Website (Seeking a PSD)

We need a user friendly website for a Home Health Care Agency. Our service is for the elderly and disabled. Frequently the busy professional middle-aged married daughter will use the website to arrange in-home care for an aging parent. Therefore, our website is primarily geared towards middle-aged women. In-home care is typically 24 hours a day so, a feeling of trustworthiness and security should be effectively conveyed. (Seeking a PSD- however, if you also offer coding, please let us know the cost.)

Target Market(s)

Frequently the busy professional middle-aged married daughter (possibly out of state) will use the website to arrange in-home care for an aging parent.

Industry/Entity Type

Security

Requirements
Must have
• Website must be clean, uncluttered and professional. The following menu pages are requested: Home, About Us, Services, Resources, FAQ, Employment & Contact.
Should not have
• Must not be too whimsical.

```html
<!DOCTYPE html>
<html lang="en">
<head>
<meta charset="utf-8">
<title>Harbor Home Health</title>
<link href="https://fonts.googleapis.com/css2?family=Bebas+Neue&family=Raleway:wght@400;500;700&display=swap" rel="stylesheet">
<style>
:root{
  --brand:#0784de;
  --nav-top:#1aa6dc;
  --nav-bottom:#27c0ef;
  --nav-line:#1288be;
  --ink:#222;
  --muted:#444;
  --white:#fff;
  --footer:#000;
  --logo:#4ea9e4;
}
*{margin:0;padding:0;box-sizing:border-box}
html,body{width:1028px;height:1200px;overflow:hidden;background:var(--white)}
body{font-family:"Raleway",sans-serif;color:var(--ink);position:relative}
.site-header{position:absolute;left:0;top:0;width:1028px;height:113px}
.brand{position:absolute;left:16px;top:14px;display:flex;align-items:center;gap:8px}
.brand-mark{width:28px;height:28px;border-radius:50%;background:var(--logo)}
.brand-name{font-weight:700;font-size:27px;line-height:27px;color:var(--logo)}
.main-nav{position:absolute;left:269px;top:5px;width:751px;height:103px;display:flex;
  background:linear-gradient(var(--nav-top),var(--nav-bottom))}
.main-nav a{flex:none;display:flex;flex-direction:column;align-items:center;justify-content:center;gap:6px;
  color:var(--white);text-decoration:none;font-size:15px;border-right:1px solid var(--nav-line)}
.main-nav a:last-child{border-right:0}
.main-nav svg{width:22px;height:20px;fill:#8fd3f3}
.hero{position:absolute;left:0;top:113px;width:1028px;height:387px;
  background:linear-gradient(100deg,#d8d6d0 0%,#cfc2b6 35%,#e7e8ea 60%,#b79e8c 85%,#a88f80 100%)}
.hero-arrow{position:absolute;top:161px;width:68px;height:68px;border-radius:50%;background:rgba(240,240,240,.9);
  display:flex;align-items:center;justify-content:center}
.hero-arrow.prev{left:19px}.hero-arrow.next{right:22px;background:rgba(225,215,210,.9)}
.hero-dots{position:absolute;left:437px;bottom:0;width:151px;height:29px;background:var(--white);
  border-radius:6px 6px 0 0;display:flex;justify-content:center;align-items:center;gap:14px}
.hero-dots span{width:12px;height:12px;border-radius:50%;background:#777}
.hero-dots span:first-child{background:#111}
.divider{position:absolute;left:180px;top:504px;width:640px;height:6px;border-radius:50%;
  background:radial-gradient(ellipse at center,rgba(0,0,0,.18),rgba(0,0,0,0) 70%)}
.about{position:absolute;left:12px;top:523px;width:525px}
.section-title{font-family:"Bebas Neue",sans-serif;font-size:31px;color:var(--brand);line-height:34px}
.about .lead{font-size:12px;line-height:13px;margin-top:4px;color:var(--ink)}
.about p.body{font-size:10.3px;line-height:12.9px;color:var(--muted);text-align:justify;margin-top:12px}
.btn-more{position:absolute;left:420px;top:777px;width:82px;height:29px;border-radius:14px;background:var(--brand);
  color:var(--white);font-size:17px;display:flex;align-items:center;justify-content:center}
.services{position:absolute;left:570px;top:532px;width:438px}
.services-head{height:49px;background:var(--brand);border-radius:12px;padding-left:16px;
  font-family:"Bebas Neue",sans-serif;font-size:25px;color:var(--white);line-height:52px}
.service{position:relative;height:128px;margin-top:10px}
.service .thumb{position:absolute;left:3px;top:0;width:84px;height:79px}
.service h3{position:absolute;left:101px;top:-3px;font-weight:400;font-size:16.5px;color:var(--brand)}
.service p{position:absolute;left:101px;top:25px;width:329px;font-size:10.3px;line-height:12.9px;text-align:justify;color:var(--ink)}
.service .read{position:absolute;left:104px;top:72px;font-size:10.5px;font-weight:500;display:flex;align-items:center;gap:5px}
.service .read svg{width:6px;height:9px;fill:var(--brand)}
.care-band{position:absolute;left:0;top:829px;width:1028px;height:312px;background:var(--brand)}
.care-band .notch{position:absolute;left:502px;width:20px;height:14px}
.care-item{position:absolute;top:50px;width:160px;text-align:center;color:var(--white)}
.care-item h4{font-weight:400;font-size:17.5px;white-space:nowrap}
.care-item .circle{width:132px;height:132px;border-radius:50%;margin:8px auto 0}
.care-item p{text-align:left;font-size:10.3px;line-height:13px;margin:12px 0 0 21px;width:145px}
.site-footer{position:absolute;left:0;top:1141px;width:1028px;height:59px;background:var(--footer);color:var(--white)}
.footer-links{position:absolute;left:14px;top:12px;font-size:12.5px}
.footer-links span{margin:0 5px}
.copyright{position:absolute;left:14px;top:35px;font-size:8px}
.social{position:absolute;left:863px;top:17px;display:flex;gap:4px}
.social span{width:30px;height:30px;border-radius:50%;background:#8a8a8a;border:2px solid #bbb}
</style>
</head>
<body>
<header class="site-header">
  <div class="brand"><span class="brand-mark"></span><span class="brand-name">Harbor<br>Home Health</span></div>
  <nav class="main-nav">
    <a href="#" style="width:88px"><svg viewBox="0 0 22 20"><path d="M11 1 1 10h3v9h5v-6h4v6h5v-9h3z"/></svg>Home</a>
    <a href="#" style="width:113px"><svg viewBox="0 0 22 20"><circle cx="6" cy="5" r="3"/><circle cx="11" cy="5" r="3"/><circle cx="16" cy="5" r="3"/><rect x="4" y="9" width="14" height="10"/></svg>About Us</a>
    <a href="#" style="width:108px"><svg viewBox="0 0 22 20"><circle cx="8" cy="12" r="5"/><circle cx="16" cy="5" r="3.5"/></svg>Services</a>
    <a href="#" style="width:120px"><svg viewBox="0 0 22 20"><circle cx="11" cy="10" r="4"/></svg>Resources</a>
    <a href="#" style="width:84px"><svg viewBox="0 0 22 20"><text x="11" y="18" text-anchor="middle" font-size="20" font-family="Raleway">?</text></svg>FAQ</a>
    <a href="#" style="width:135px"><svg viewBox="0 0 22 20"><circle cx="8" cy="6" r="4"/><circle cx="15" cy="6" r="4"/><rect x="2" y="11" width="18" height="8" rx="3"/></svg>Employment</a>
    <a href="#" style="width:103px"><svg viewBox="0 0 22 20"><path d="M2 7 11 2l9 5v11H2z"/></svg>Contact.</a>
  </nav>
</header>

<section class="hero" role="img" aria-label="Photo of a smiling elderly man with a caregiver's hand on his shoulder">
  <span class="hero-arrow prev"><svg width="22" height="26" viewBox="0 0 22 26"><path d="M17 2 5 13l12 11" fill="none" stroke="#333" stroke-width="5"/></svg></span>
  <span class="hero-arrow next"><svg width="22" height="26" viewBox="0 0 22 26"><path d="M5 2l12 11L5 24" fill="none" stroke="#333" stroke-width="5"/></svg></span>
  <div class="hero-dots"><span></span><span></span><span></span><span></span></div>
</section>
<div class="divider"></div>

<section class="about">
  <h2 class="section-title">About Us</h2>
  <p class="lead">Sed ut perspiciatis unde omnis iste natus error sit voluptatem accusantium doloremque laudantium,</p>
  <p class="body">Li Europan lingues es membres del sam familie. Lor separat existentie es un myth. Por scientie, musica, sport etc, litot Europa usa li sam vocabular. Li lingues differe solmen in li grammatica, li pronunciation e li plu commun vocabules. Omnicos directe al desirabilite de un nov lingua franca: On refusa continuar payar custosi traductores. At solmen va esser necessi far uniform grammatica, pronunciation e plu sommun paroles. Ma quande lingues coalesce, li grammatica del resultant lingue es plu simplic e regulari quam ti del coalescent lingues. Li nov lingua franca va esser plu simplic</p>
  <p class="body">Li Europan lingues es membres del sam familie. Lor separat existentie es un myth. Por scientie, musica, sport etc, litot Europa usa li sam vocabular. Li lingues differe solmen in li grammatica, li pronunciation e li plu commun vocabules. Omnicos directe al desirabilite de un nov lingua franca: On refusa continuar payar custosi traductores. At solmen va esser necessi far uniform grammatica, pronunciation e plu sommun paroles. Ma quande lingues coalesce, li grammatica del resultant lingue es plu simplic e regulari quam ti del coalescent lingues. Li nov lingua franca va esser plu simplic</p>
</section>
<a class="btn-more" href="#">MORE</a>

<section class="services">
  <h2 class="services-head">Our Services</h2>
  <article class="service">
    <div class="thumb" role="img" aria-label="Photo of elderly hands resting on a cane" style="background:linear-gradient(135deg,#e9d2bf,#b07f62)"></div>
    <h3>Epidemiology</h3>
    <p>Disability is an umbrella term, covering impairments, activity limitations, and participation restrictions. An impairment is a problem in body function or structure</p>
    <span class="read">READ MORE <svg viewBox="0 0 6 9"><path d="M0 0l6 4.5L0 9z"/></svg></span>
  </article>
  <article class="service">
    <div class="thumb" role="img" aria-label="Photo of an elderly woman with a caregiver" style="background:linear-gradient(135deg,#b88d74,#e6e1dd)"></div>
    <h3>Aetiology</h3>
    <p>Disability is an umbrella term, covering impairments, activity limitations, and participation restrictions. An impairment is a problem in body function or structure</p>
    <span class="read">READ MORE <svg viewBox="0 0 6 9"><path d="M0 0l6 4.5L0 9z"/></svg></span>
  </article>
</section>

<section class="care-band">
  <svg class="notch" style="top:0" viewBox="0 0 20 14"><path d="M0 0h20L10 14z" fill="#fff"/></svg>
  <svg class="notch" style="bottom:0" viewBox="0 0 20 14"><path d="M0 14h20L10 0z" fill="#000"/></svg>
  <div class="care-item" style="left:96px"><h4>Heart problems</h4><div class="circle" role="img" aria-label="Photo of a smiling elderly woman" style="background:linear-gradient(135deg,#f3ece4,#e3559a)"></div><p>The number of people aged 65 and over is estimated to increase by 65% in the next 25 years,</p></div>
  <div class="care-item" style="left:260px"><h4>Hearing impairment.</h4><div class="circle" role="img" aria-label="Photo of a nurse checking an elderly woman's blood pressure" style="background:linear-gradient(135deg,#e8dccb,#6d6a72)"></div><p>The number of people aged 65 and over is estimated to increase by 65% in the next 25 years,</p></div>
  <div class="care-item" style="left:430px"><h4>Foot problems</h4><div class="circle" role="img" aria-label="Photo of a caregiver helping an elderly man" style="background:linear-gradient(135deg,#d9d3cd,#e97b3c)"></div><p>The number of people aged 65 and over is estimated to increase by 65% in the next 25 years,</p></div>
  <div class="care-item" style="left:604px"><h4>Risk factors</h4><div class="circle" role="img" aria-label="Photo of a caregiver and an elderly woman reading together" style="background:linear-gradient(135deg,#c9b8a8,#6f5e55)"></div><p>The number of people aged 65 and over is estimated to increase by 65% in the next 25 years,</p></div>
  <div class="care-item" style="left:780px"><h4>Epidemiology</h4><div class="circle" role="img" aria-label="Photo of an elderly hand holding a cane" style="background:linear-gradient(135deg,#c79a74,#5c4433)"></div><p>The number of people aged 65 and over is estimated to increase by 65% in the next 25 years,</p></div>
</section>

<footer class="site-footer">
  <div class="footer-links">Home<span>|</span>About Us<span>|</span>Services<span>|</span>Resources<span>|</span>FAQ<span>|</span>Employment<span>|</span>Contact.</div>
  <div class="copyright">Copy (c) www.harborhomehealth.com. All Right Reserve</div>
  <div class="social"><span></span><span></span><span></span><span></span></div>
</footer>
</body>
</html>
```